Predictive Analytics User Interface

We need a User Interface for web application to be used by School District administrators in the United States. The software is a Predictive Analytics application that will allow a school district administrators to see Predictions of how a campus will perform in the following categories:

State Assessment Exams (example: Will a specific grade level (3rd, 4th, 5th, etc.) achieve their target test scores in May, 2017)
Graduation Rates (example: Will the 12th grade class graduation rate achieve their goal of 98% graduation rate by May, 2017)
Drop-Out Rates (example: Will the current 9th grade class have a drop-out rate lower than 5% in the next four years (assuming it takes all 9th graders 4 years to graduate from US high schools).

We are looking for sleek but simple. The design must support the data - not detract from it.

Target Market(s)

Public Education in Grades 1-12 and Higher Education for 2-year and 4-year colleges.

Industry/Entity Type

Education

Number of Pages Required

3 page

Font styles to use
Sans Serif

Colors
f78f20
9bcb3c
ec1f27
6b449b
0455a3

Requirements
Must have
• Ability to segment student groups into four probability categories: Excellent, Good, Fair, and Poor. Additionally, each student group should have "Action Buttons" that show an activity for each student group. For example, let's say a School Principal looks at their screen and clicks on High School Graduation. They would get students in four groups. If the "Poor" category showed 12% of the school, the Principal would have "Action Buttons" like "Assign to Tutoring" or "Meet with Counselor" to address their needs. The goal is not just to identify student groups but also be able to take action directly from the UI.
Nice to have
• Drill-down capabilities in each group that shows me deeper details. For example, if a School Principal looked at the High School Graduation section and clicked on "Poor" which showed a Student Group with low probability of graduating from high school, it would be nice if the principal could click on a "See Details" and see another layer of data explaining why the Prediction believes these students will drop out. As an example, it could show a report of 10+ absences, 15+ behavior issues reported, and failing 2 classes. It could also show recommendations as to improve their probability with different interventions like "sign up for tutoring" or "assign a mentor".
Should not have
• Small print, small charts and colors difficult to read. Our target audience is people between the age of 50-70, so their eyesight is not always the best. We are looking for simple and clean but bold enough that your grandmother could view it and have a discussion about the data.

```html
<!DOCTYPE html>
<html lang="en">
<head>
<meta charset="utf-8">
<title>Brightpath Dashboard</title>
<link href="https://fonts.googleapis.com/css2?family=Montserrat:wght@500;600;700&family=Nunito+Sans:wght@400;600;700&display=swap" rel="stylesheet">
<style>
:root{
  --poor:#0455a3;--fair:#9bcb3c;--good:#f78f20;--excellent:#2ecc71;
  --purple:#6b449b;--sky:#3aa0d8;--ink:#333;--muted:#8a8f96;--icon:#a9adb2;
  --panel:#23262e;--profile:#3a3f48;--page:#eef0f0;--side:#f5f5f5;--line:#e3e6e8;
}
*{box-sizing:border-box;margin:0;padding:0}
html,body{width:1200px;height:789px;overflow:hidden;background:var(--page)}
body{font-family:"Nunito Sans",sans-serif;color:var(--ink)}
.stage{position:absolute;left:0;top:0;width:1400px;height:921px;transform:scale(.857143);transform-origin:0 0;background:var(--page)}
.abs{position:absolute}
.topbar{left:0;top:0;width:1400px;height:62px;background:#fff;box-shadow:0 2px 4px rgba(0,0,0,.12);z-index:2}
.brand{left:14px;top:12px;font-family:"Montserrat",sans-serif;font-weight:700;font-size:28px;letter-spacing:2px;color:#1d6e73}
.sidebar{left:0;top:62px;width:249px;height:859px;background:var(--side)}
.profile{left:0;top:62px;width:249px;height:172px;background:var(--profile);color:#fff;text-align:center}
.avatar{position:absolute;left:82px;top:18px;width:84px;height:84px;border-radius:50%;background:radial-gradient(circle at 50% 40%,#c98a63,#6b3d26)}
.online{position:absolute;left:158px;top:52px;width:12px;height:12px;border-radius:50%;background:#3ccf4e}
.kebab{position:absolute;left:226px;top:12px;width:8px}
.kebab i{display:block;width:7px;height:7px;border-radius:50%;background:#9aa0a8;margin-bottom:4px}
.profile .name{position:absolute;left:0;right:0;top:110px;font-size:17px;font-weight:600}
.profile .role{position:absolute;left:0;right:0;top:133px;font-size:13px;color:#c7ccd2}
.accent{left:0;top:234px;width:249px;height:8px;background:var(--sky)}
.nav{left:0;top:242px;width:249px;list-style:none}
.nav li{height:52px;display:flex;align-items:center;padding-left:34px;font-size:14px;color:var(--muted);gap:10px}
.nav li.active{background:#e8e9ea;color:#666;font-weight:600;padding-left:28px;gap:6px}
.nav svg{flex:none}
.card{background:#fff;box-shadow:0 1px 3px rgba(0,0,0,.12)}
.stat{top:92px;width:254px;height:176px}
.stat .num{position:absolute;left:21px;top:18px;font-family:"Montserrat",sans-serif;font-weight:700;font-size:40px;color:#5a5f66}
.stat .lbl{position:absolute;left:21px;top:67px;font-size:13px;color:#9a9ea4;letter-spacing:.3px}
.stat .bar{position:absolute;left:21px;top:97px;width:213px;height:4px;background:#eceeef}
.stat .bar b{display:block;height:4px}
.stat .btn{position:absolute;left:21px;top:120px;width:213px;height:34px;color:#fff;font-size:14px;font-weight:600;padding:8px 10px}
.stat svg{position:absolute;right:20px;top:18px}
.tabs{left:274px;top:297px;width:1105px;height:42px;display:flex;align-items:center;font-size:15px}
.tab{display:flex;align-items:center;gap:10px;padding:0 17px;height:42px}
.tab.on{border-bottom:2px solid var(--sky)}
.tabs .right{margin-left:auto;display:flex;gap:30px;padding-right:20px;align-items:center}
.chartcard{left:274px;top:369px;width:590px;height:520px}
.chartcard h3{position:absolute;left:19px;top:32px;font-size:16px;font-weight:400}
.legend{position:absolute;left:21px;top:82px;display:flex;gap:36px;font-size:13px;font-weight:700;color:#555}
.legend span{border-left:4px solid;padding-left:6px}
.analytics{left:894px;top:369px;width:486px;height:176px;background:var(--panel);color:#fff;font-family:"Montserrat",sans-serif}
.analytics .t{position:absolute;font-size:14px;font-weight:600}
.grid{position:absolute;left:228px;top:50px;font-size:11px;font-weight:600;border-collapse:collapse}
.grid th{font-size:12px;text-align:left;padding-bottom:8px}
.grid td{padding:4px 0;height:23px}
.sw{display:inline-block;width:12px;height:12px;vertical-align:-2px;margin-right:10px}
.tile{top:589px;width:230px;height:300px;text-align:center;overflow:hidden}
.tile .cap{position:absolute;left:0;right:0;top:170px;font-size:17px;color:#555;line-height:19px}
.tile svg{position:absolute;left:0;top:0}
</style>
</head>
<body>
<div class="stage">
  <header class="abs topbar">
    <div class="abs brand">BRIGHTPATH</div>
    <svg class="abs" style="left:280px;top:19px" width="22" height="20"><rect y="1" width="22" height="3" fill="#222"/><rect y="8" width="22" height="3" fill="#222"/><rect y="15" width="22" height="3" fill="#222"/></svg>
    <svg class="abs" style="left:334px;top:18px" width="22" height="22"><circle cx="11" cy="11" r="11" fill="#111"/><rect x="9.5" y="4" width="3" height="9" fill="#fff"/><rect x="9.5" y="15" width="3" height="3" fill="#fff"/></svg>
    <svg class="abs" style="left:1268px;top:22px" width="18" height="18"><circle cx="9" cy="5" r="4.5" fill="#333"/><path d="M1 17c0-6 16-6 16 0z" fill="#333"/></svg>
    <svg class="abs" style="left:1310px;top:16px" width="26" height="24"><path d="M3 19c3-3 2-11 7-12 5 1 4 9 7 12z" fill="#333"/><circle cx="10" cy="20" r="2" fill="#333"/><circle cx="16" cy="7" r="6" fill="#f78f20"/></svg>
    <svg class="abs" style="left:1352px;top:16px" width="26" height="24"><rect x="1" y="8" width="18" height="12" fill="none" stroke="#333" stroke-width="2"/><path d="M1 8l9 7 9-7" fill="none" stroke="#333" stroke-width="2"/><circle cx="17" cy="7" r="6" fill="#ec1f27"/></svg>
  </header>

  <aside class="abs sidebar"></aside>
  <div class="abs profile">
    <div class="avatar" role="img" aria-label="Profile photo of the HR admin"></div>
    <div class="online"></div>
    <div class="kebab"><i></i><i></i><i></i></div>
    <div class="name">Lorem ipsum</div>
    <div class="role">HR Admin</div>
  </div>
  <div class="abs accent"></div>
  <ul class="abs nav">
    <li class="active"><svg width="30" height="30"><circle cx="15" cy="15" r="15" fill="var(--sky)"/><path d="M7 15l8-7 8 7h-2v6h-4v-4h-4v4H9v-6z" fill="#fff"/></svg>Dashboard</li>
    <li><svg width="20" height="18" fill="var(--icon)"><circle cx="7" cy="10" r="5"/><circle cx="15" cy="5" r="3.5"/><circle cx="7" cy="10" r="2" fill="var(--side)"/><circle cx="15" cy="5" r="1.3" fill="var(--side)"/></svg>Settings</li>
    <li><svg width="20" height="18" fill="var(--icon)"><circle cx="5" cy="5" r="3"/><circle cx="15" cy="5" r="3"/><circle cx="10" cy="7" r="3.5"/><path d="M0 14c0-4 6-5 8-4 2-1 8 0 8 4v3H0z"/><path d="M12 10c4-1 8 0 8 4v3h-4z"/></svg>Academic</li>
    <li><svg width="20" height="18"><path d="M1 9q9-10 18 0q-9 10-18 0z" fill="var(--icon)"/><circle cx="10" cy="9" r="3" fill="var(--side)"/></svg>HR/Payroll</li>
    <li><svg width="20" height="18" fill="var(--icon)"><circle cx="10" cy="5" r="4"/><path d="M3 17c0-6 14-6 14 0z"/></svg>Student</li>
    <li><svg width="20" height="18"><rect x="1" y="4" width="18" height="11" fill="var(--icon)"/><circle cx="10" cy="9.5" r="3" fill="var(--side)"/></svg>Finance</li>
    <li><svg width="20" height="18"><path d="M5 2h12l-3 14H2z" fill="var(--icon)"/><path d="M6 5h8M5 8h8" stroke="var(--side)" stroke-width="1.3"/></svg>Library</li>
    <li><svg width="20" height="18" fill="var(--icon)"><rect x="0" y="3" width="12" height="10"/><path d="M12 6h4l3 4v3h-7z"/><circle cx="4" cy="14" r="2.5"/><circle cx="15" cy="14" r="2.5"/></svg>Transport</li>
    <li><svg width="20" height="18" fill="var(--icon)"><rect x="0" y="3" width="2" height="13"/><rect x="0" y="10" width="20" height="3"/><rect x="18" y="8" width="2" height="8"/><rect x="3" y="6" width="4" height="4"/><rect x="8" y="6" width="10" height="4"/></svg>Hostel</li>
    <li><svg width="20" height="18"><rect x="1" y="3" width="18" height="12" fill="var(--icon)"/><path d="M1 4l9 6 9-6" fill="none" stroke="var(--side)" stroke-width="1.4"/></svg>Messages/SMS</li>
    <li><svg width="20" height="18" fill="var(--icon)"><rect x="1" y="3" width="3" height="3"/><rect x="6" y="3" width="13" height="3"/><rect x="1" y="8" width="3" height="3"/><rect x="6" y="8" width="13" height="3"/><rect x="1" y="13" width="3" height="3"/><rect x="6" y="13" width="13" height="3"/></svg>Store Management</li>
  </ul>

  <section class="abs card stat" style="left:274px">
    <div class="num">1520</div><div class="lbl">POOR STUDENTS</div>
    <svg width="42" height="42"><circle cx="21" cy="21" r="19" fill="none" stroke="var(--poor)" stroke-width="2"/><circle cx="15" cy="17" r="1.8" fill="var(--poor)"/><circle cx="27" cy="17" r="1.8" fill="var(--poor)"/><path d="M13 30q8-8 16 0" fill="none" stroke="var(--poor)" stroke-width="2"/></svg>
    <div class="bar"><b style="width:91%;background:var(--poor)"></b></div>
    <div class="btn" style="background:var(--poor)">Read full report</div>
  </section>
  <section class="abs card stat" style="left:558px">
    <div class="num">758</div><div class="lbl">FAIR STUDENTS</div>
    <svg width="42" height="42"><circle cx="21" cy="21" r="19" fill="none" stroke="var(--fair)" stroke-width="2"/><circle cx="15" cy="17" r="1.8" fill="var(--fair)"/><circle cx="27" cy="17" r="1.8" fill="var(--fair)"/><path d="M14 27h14" stroke="var(--fair)" stroke-width="2"/></svg>
    <div class="bar"><b style="width:70%;background:var(--fair)"></b></div>
    <div class="btn" style="background:var(--fair)">Read full report</div>
  </section>
  <section class="abs card stat" style="left:842px">
    <div class="num">375</div><div class="lbl">GOOD STUDENTS</div>
    <svg width="42" height="42"><circle cx="21" cy="21" r="19" fill="none" stroke="var(--good)" stroke-width="2"/><path d="M12 16q3-3 6 0M24 16q3-3 6 0" fill="none" stroke="var(--good)" stroke-width="2"/><path d="M13 25q8 7 16 0" fill="none" stroke="var(--good)" stroke-width="2"/></svg>
    <div class="bar"><b style="width:70%;background:var(--good)"></b></div>
    <div class="btn" style="background:var(--good)">Read full report</div>
  </section>
  <section class="abs card stat" style="left:1125px">
    <div class="num">250</div><div class="lbl">EXCELLENT</div>
    <svg width="42" height="42"><circle cx="21" cy="21" r="19" fill="none" stroke="var(--excellent)" stroke-width="2"/><path d="M12 16q3-3 6 0M24 16q3-3 6 0" fill="none" stroke="var(--excellent)" stroke-width="2"/><path d="M13 25q8 7 16 0" fill="none" stroke="var(--excellent)" stroke-width="2"/></svg>
    <div class="bar"><b style="width:30%;background:var(--excellent)"></b></div>
    <div class="btn" style="background:var(--excellent)">Read full report</div>
  </section>

  <nav class="abs card tabs">
    <div class="tab on"><svg width="14" height="12"><rect y="0" width="14" height="2" fill="#222"/><rect y="5" width="14" height="2" fill="#222"/><rect y="10" width="14" height="2" fill="#222"/></svg>Activity</div>
    <div class="tab"><svg width="16" height="16"><rect x="1" y="2.5" width="14" height="12.5" fill="none" stroke="#333" stroke-width="1.2"/><rect x="1" y="2.5" width="14" height="3" fill="#333"/><path d="M4.5 0.5v3M11.5 0.5v3" stroke="#333" stroke-width="1.4"/><g fill="#333"><rect x="3" y="7.5" width="2" height="2"/><rect x="7" y="7.5" width="2" height="2"/><rect x="11" y="7.5" width="2" height="2"/><rect x="3" y="11" width="2" height="2"/><rect x="7" y="11" width="2" height="2"/><rect x="11" y="11" width="2" height="2"/></g></svg>Schedule</div>
    <div class="tab"><svg width="16" height="16"><rect x="1" y="2.5" width="14" height="12.5" fill="none" stroke="#333" stroke-width="1.2"/><rect x="1" y="2.5" width="14" height="3" fill="#333"/><path d="M4.5 0.5v3M11.5 0.5v3" stroke="#333" stroke-width="1.4"/><g fill="#333"><rect x="3" y="7.5" width="2" height="2"/><rect x="7" y="7.5" width="2" height="2"/><rect x="11" y="7.5" width="2" height="2"/><rect x="3" y="11" width="2" height="2"/><rect x="7" y="11" width="2" height="2"/><rect x="11" y="11" width="2" height="2"/></g></svg>Fee reports</div>
    <div class="right">
      <svg width="34" height="16"><g fill="#222"><rect x="0" y="0" width="4" height="4"/><rect x="6" y="0" width="4" height="4"/><rect x="12" y="0" width="4" height="4"/><rect x="0" y="6" width="4" height="4"/><rect x="6" y="6" width="4" height="4"/><rect x="12" y="6" width="4" height="4"/><rect x="0" y="12" width="4" height="4"/><rect x="6" y="12" width="4" height="4"/><rect x="12" y="12" width="4" height="4"/></g><path d="M26 6l3 3 3-3" fill="none" stroke="#444" stroke-width="1.3"/></svg>
      <span style="display:flex;gap:10px;align-items:center"><svg width="17" height="15"><path d="M4 1h12v10H4z" fill="none" stroke="#333" stroke-width="1.2"/><path d="M1 4h3v10h10v-3" fill="none" stroke="#333" stroke-width="1.2"/><path d="M7 4h6M7 6.5h6M7 9h4" stroke="#333"/></svg>Support</span>
    </div>
  </nav>

  <section class="abs card chartcard">
    <h3>Daily Attendance Overview</h3>
    <div class="legend"><span style="border-color:var(--purple)">SECONDARY</span><span style="border-color:var(--sky)">HIGHER</span><span style="border-color:var(--good)">COLLEGE</span></div>
    <svg width="590" height="520" viewBox="274 369 590 520" style="position:absolute;left:0;top:0" font-family="Nunito Sans, sans-serif" font-size="16" fill="#555">
      <g stroke="#eceeef">
        <line x1="345" y1="516" x2="832" y2="516"/><line x1="345" y1="564" x2="832" y2="564"/><line x1="345" y1="612" x2="832" y2="612"/><line x1="345" y1="659" x2="832" y2="659"/><line x1="345" y1="707" x2="832" y2="707"/><line x1="345" y1="755" x2="832" y2="755"/><line x1="345" y1="802" x2="832" y2="802"/>
        <line x1="345" y1="506" x2="345" y2="802"/><line x1="425" y1="506" x2="425" y2="802"/><line x1="507" y1="506" x2="507" y2="802"/><line x1="581" y1="506" x2="581" y2="802"/><line x1="661" y1="506" x2="661" y2="802"/><line x1="744" y1="506" x2="744" y2="802"/><line x1="821" y1="506" x2="821" y2="802"/>
      </g>
      <g text-anchor="end"><text x="328" y="522">30</text><text x="328" y="570">25</text><text x="328" y="618">20</text><text x="328" y="665">15</text><text x="328" y="713">10</text><text x="324" y="761">5</text><text x="324" y="808">0</text></g>
      <g text-anchor="middle"><text x="345" y="830">18/12</text><text x="425" y="830">19/12</text><text x="507" y="830">20/12</text><text x="581" y="830">21/12</text><text x="661" y="830">22/12</text><text x="744" y="830">Today</text><text x="821" y="830">24/12</text></g>
      <polygon fill="#f7a957" opacity=".75" points="347,802 347,745 362,628 410,648 458,628 502,573 560,630 640,578 668,660 698,556 740,648 742,802"/>
      <polygon fill="#6cbcd9" opacity=".75" points="347,802 352,660 410,676 435,658 478,616 497,660 520,668 605,575 660,686 690,612 740,650 742,802"/>
      <polygon fill="#6b4f9e" opacity=".75" points="347,802 347,682 405,698 478,726 548,628 600,697 643,742 697,718 742,708 742,802"/>
    </svg>
    <svg style="position:absolute;right:24px;top:38px" width="36" height="14"><path d="M0 4l4 4 4-4" fill="none" stroke="#333" stroke-width="1.5"/><path d="M28 2a5 5 0 1 0 4 3" fill="none" stroke="#333" stroke-width="1.5"/><path d="M30 0l3 2-3 2" fill="none" stroke="#333" stroke-width="1.3"/></svg>
  </section>

  <section class="abs analytics">
    <div class="t" style="left:20px;top:16px">PREDICTIVE ANALYTICS</div>
    <div style="position:absolute;left:209px;top:18px;width:1px;height:140px;background:#3b3f48"></div>
    <div class="t" style="left:228px;top:16px">STUDENT GRADE</div>
    <div class="t" style="left:368px;top:16px">CLASS RANGE</div>
    <svg width="140" height="130" viewBox="900 405 140 130" style="position:absolute;left:6px;top:36px" font-family="Montserrat, sans-serif" font-weight="600" font-size="16" fill="#fff">
      <path d="M971 472L930.7 431.7A57 57 0 0 1 1011.3 431.7Z" fill="#3aa9d4"/>
      <path d="M971 472L1011.3 431.7A57 57 0 0 1 1021.8 497.9Z" fill="#a5c8e6"/>
      <path d="M971 472L1021.8 497.9A57 57 0 0 1 979.9 528.3Z" fill="#e05a0c"/>
      <path d="M971 472L979.9 528.3A57 57 0 0 1 930.7 431.7Z" fill="var(--purple)"/>
      <text x="960" y="447">25%</text><text x="990" y="476">20%</text><text x="982" y="504">15%</text><text x="928" y="492">40%</text>
    </svg>
    <table class="grid">
      <tr><th style="width:110px">GRADE ITEM</th><th style="width:77px">GRADE</th><th>WEIGHT</th></tr>
      <tr><td><span class="sw" style="background:#e05a0c"></span>AT</td><td>100%</td><td>15%</td></tr>
      <tr><td><span class="sw" style="background:#a5c8e6"></span>PROJECT</td><td>100%</td><td>20%</td></tr>
      <tr><td><span class="sw" style="background:#3aa9d4"></span>PAPERS</td><td>35%</td><td>25%</td></tr>
      <tr><td><span class="sw" style="background:var(--purple)"></span>QUIZZES</td><td>98%</td><td>40%</td></tr>
    </table>
  </section>

  <section class="abs card tile" style="left:891px">
    <svg width="230" height="300">
      <path d="M61 76A60 60 0 1 0 114 16" fill="none" stroke="var(--good)" stroke-width="2"/>
      <g fill="none" stroke="var(--good)" stroke-width="2"><path d="M100 56h28v12a14 14 0 0 1-28 0z"/><path d="M100 60h-6q0 10 8 12M128 60h6q0 10-8 12"/><path d="M114 82v10M104 92h20v8h-20z"/><path d="M114 62l2 4h4l-3 3 1 4-4-2-4 2 1-4-3-3h4z"/></g>
      <g fill="var(--good)">
        <rect x="29" y="258" width="3" height="42"/><rect x="34" y="252" width="3" height="48"/><rect x="39" y="246" width="3" height="54"/><rect x="44" y="256" width="3" height="44"/><rect x="49" y="242" width="3" height="58"/><rect x="54" y="250" width="3" height="50"/><rect x="59" y="260" width="3" height="40"/><rect x="64" y="254" width="3" height="46"/><rect x="69" y="246" width="3" height="54"/><rect x="74" y="258" width="3" height="42"/><rect x="79" y="248" width="3" height="52"/><rect x="84" y="262" width="3" height="38"/><rect x="89" y="252" width="3" height="48"/><rect x="94" y="244" width="3" height="56"/><rect x="99" y="256" width="3" height="44"/><rect x="104" y="240" width="3" height="60"/><rect x="109" y="250" width="3" height="50"/><rect x="114" y="258" width="3" height="42"/><rect x="119" y="246" width="3" height="54"/><rect x="124" y="254" width="3" height="46"/><rect x="129" y="242" width="3" height="58"/><rect x="134" y="252" width="3" height="48"/><rect x="139" y="260" width="3" height="40"/><rect x="144" y="248" width="3" height="52"/><rect x="149" y="256" width="3" height="44"/><rect x="154" y="244" width="3" height="56"/><rect x="159" y="254" width="3" height="46"/><rect x="164" y="262" width="3" height="38"/><rect x="169" y="250" width="3" height="50"/><rect x="174" y="246" width="3" height="54"/><rect x="179" y="258" width="3" height="42"/><rect x="184" y="248" width="3" height="52"/><rect x="189" y="252" width="3" height="48"/><rect x="194" y="256" width="3" height="44"/><rect x="199" y="254" width="3" height="46"/>
      </g>
    </svg>
    <div class="cap">Total Alumni<br>Members</div>
  </section>

  <section class="abs card tile" style="left:1150px">
    <svg width="230" height="300">
      <path d="M115 16A60 60 0 1 1 64 107" fill="none" stroke="var(--poor)" stroke-width="2"/>
      <path d="M64 107A60 60 0 0 1 115 16" fill="none" stroke="#dde0e3" stroke-width="1"/>
      <g fill="none" stroke="var(--poor)" stroke-width="2.5"><circle cx="117" cy="65" r="11"/><path d="M97 96q0-16 20-16t20 16q-20 10-40 0z"/></g>
      <g fill="var(--poor)">
        <rect x="29" y="260" width="3" height="40"/><rect x="34" y="254" width="3" height="46"/><rect x="39" y="244" width="3" height="56"/><rect x="44" y="252" width="3" height="48"/><rect x="49" y="258" width="3" height="42"/><rect x="54" y="248" width="3" height="52"/><rect x="59" y="256" width="3" height="44"/><rect x="64" y="250" width="3" height="50"/><rect x="69" y="260" width="3" height="40"/><rect x="74" y="246" width="3" height="54"/><rect x="79" y="254" width="3" height="46"/><rect x="84" y="262" width="3" height="38"/><rect x="89" y="258" width="3" height="42"/><rect x="94" y="250" width="3" height="50"/><rect x="99" y="242" width="3" height="58"/><rect x="104" y="256" width="3" height="44"/><rect x="109" y="248" width="3" height="52"/><rect x="114" y="260" width="3" height="40"/><rect x="119" y="252" width="3" height="48"/><rect x="124" y="246" width="3" height="54"/><rect x="129" y="258" width="3" height="42"/><rect x="134" y="242" width="3" height="58"/><rect x="139" y="250" width="3" height="50"/><rect x="144" y="256" width="3" height="44"/><rect x="149" y="248" width="3" height="52"/><rect x="154" y="260" width="3" height="40"/><rect x="159" y="252" width="3" height="48"/><rect x="164" y="244" width="3" height="56"/><rect x="169" y="256" width="3" height="44"/><rect x="174" y="262" width="3" height="38"/><rect x="179" y="250" width="3" height="50"/><rect x="184" y="246" width="3" height="54"/><rect x="189" y="258" width="3" height="42"/><rect x="194" y="252" width="3" height="48"/><rect x="199" y="256" width="3" height="44"/>
      </g>
    </svg>
    <div class="cap">Total<br>Admin Users</div>
  </section>
</div>
</body>
</html>
```